Coffee and Plastics

I am looking for a completely new site that shows the products we have. Our current site is www.morvelbrewsupply.com. We are open minded to what designers come up with. Our current site is www.morvelbrewsupply.com. You can you the information from there to start the site. I need these tabs on the main home page. ( Home, Coffee & Tea, Condiments, and Paper and Plastics, and Contact.) You can take photos and info from my Current site. In products page.
I will be uploading info and photo for paper and plastics.
Look and feel
Each slider illustrates characteristics of the customer's brand and the style your logo design should communicate.

```html
<!DOCTYPE html>
<html lang="en">
<head>
<meta charset="utf-8">
<title>Morvel Brew Supply</title>
<link href="https://fonts.googleapis.com/css2?family=Source+Sans+3:wght@600;700&family=Lexend:wght@500&display=swap" rel="stylesheet">
<style>
  :root {
    --header-top: #3a3633;
    --header-bottom: #1f1c1a;
    --logo-text: #d9d4cc;
    --nav-text: #d6d0c6;
    --nav-active-bg: #ffffff;
    --nav-active-text: #1c1a18;
    --page-bg: #e9d3a4;
    --page-bg-light: #f0dfb8;
    --card-head-top: #7a5327;
    --card-head-bottom: #3f2711;
    --card-head-text: #f3e7d2;
    --card-border: #b59a6c;
    --caption-bg: rgba(10, 8, 6, 0.85);
    --caption-text: #f2eee8;
  }
  * { margin: 0; padding: 0; box-sizing: border-box; }
  html, body { width: 1200px; height: 938px; overflow: hidden; }
  body {
    position: relative;
    background: radial-gradient(ellipse at 50% 40%, var(--page-bg-light), var(--page-bg) 70%);
    font-family: "Source Sans 3", "Source Sans Pro", sans-serif;
  }
  .site-header {
    position: absolute; left: 0; top: 0; width: 1200px; height: 56px;
    background: linear-gradient(var(--header-top), var(--header-bottom));
    z-index: 2;
  }
  .brand {
    position: absolute; left: 158px; top: 20px;
    font-size: 24px; font-weight: 700; color: var(--logo-text); letter-spacing: 0.1px;
  }
  .main-nav { position: absolute; top: 23px; left: 0; width: 1200px; height: 19px; }
  .main-nav a {
    position: absolute; top: 0; height: 19px; line-height: 19px;
    font-size: 14px; font-weight: 700; color: var(--nav-text);
    text-decoration: none; letter-spacing: 0.2px; white-space: nowrap;
  }
  .main-nav a.is-active {
    background: var(--nav-active-bg); color: var(--nav-active-text);
    border-radius: 3px; padding: 0 5px;
  }
  .hero {
    position: absolute; left: 0; top: 56px; width: 1200px; height: 526px;
    background:
      radial-gradient(ellipse 22% 26% at 50% 70%, rgba(150,85,35,0.9), rgba(150,85,35,0) 75%),
      radial-gradient(ellipse 30% 22% at 72% 62%, rgba(135,75,30,0.85), rgba(135,75,30,0) 75%),
      radial-gradient(ellipse 28% 22% at 30% 72%, rgba(120,65,25,0.85), rgba(120,65,25,0) 75%),
      radial-gradient(ellipse 24% 38% at 8% 68%, rgba(196,150,92,0.95), rgba(196,150,92,0) 72%),
      radial-gradient(ellipse 18% 40% at 94% 58%, rgba(190,145,88,0.9), rgba(190,145,88,0) 72%),
      radial-gradient(ellipse 50% 18% at 55% 38%, rgba(170,125,75,0.7), rgba(170,125,75,0) 75%),
      radial-gradient(ellipse 12% 10% at 20% 20%, rgba(220,210,200,0.35), rgba(220,210,200,0) 80%),
      radial-gradient(ellipse 10% 10% at 46% 8%, rgba(220,210,200,0.3), rgba(220,210,200,0) 80%),
      radial-gradient(ellipse 10% 10% at 72% 12%, rgba(220,210,200,0.3), rgba(220,210,200,0) 80%),
      linear-gradient(#0c0604 0%, #2a160a 32%, #4a2810 60%, #3a1e0c 85%, #6b4a2a 100%);
  }
  .hero-caption {
    position: absolute; left: 150px; top: 406px; width: 900px; height: 73px;
    background: var(--caption-bg);
    display: flex; align-items: center; justify-content: center;
    font-family: "Lexend", sans-serif; font-weight: 500; font-size: 21px; letter-spacing: 1.4px;
    color: var(--caption-text); text-transform: uppercase; white-space: nowrap;
  }
  .product-card {
    position: absolute; top: 628px; width: 282px; height: 330px;
    border: 1px solid var(--card-border); border-radius: 3px 3px 0 0; overflow: hidden;
  }
  .product-card h2 {
    height: 47px; line-height: 48px; text-align: center;
    background: linear-gradient(var(--card-head-top), var(--card-head-bottom));
    color: var(--card-head-text); font-size: 18px; font-weight: 700; letter-spacing: 2px;
  }
  .product-photo { height: 283px; }
  .photo-coffee {
    background:
      radial-gradient(ellipse 45% 55% at 48% 70%, #8e2a1c 0%, #6e1e14 60%, rgba(110,30,20,0) 100%),
      radial-gradient(ellipse 25% 20% at 50% 45%, rgba(190,140,60,0.8), rgba(190,140,60,0) 80%),
      linear-gradient(180deg, #c9c2b6 0%, #a59c8f 60%, #8c8478 100%);
  }
  .photo-tea {
    background:
      radial-gradient(ellipse 40% 22% at 50% 22%, rgba(45,70,150,0.95), rgba(45,70,150,0) 85%),
      radial-gradient(ellipse 45% 30% at 50% 55%, rgba(170,110,50,0.85), rgba(170,110,50,0) 85%),
      radial-gradient(ellipse 45% 18% at 45% 85%, rgba(70,130,80,0.8), rgba(70,130,80,0) 85%),
      linear-gradient(180deg, #f3efe8, #e6dfd2);
  }
  .photo-condiments {
    background:
      radial-gradient(ellipse 50% 30% at 45% 90%, rgba(140,100,60,0.85), rgba(140,100,60,0) 80%),
      radial-gradient(ellipse 20% 40% at 58% 35%, rgba(205,205,205,0.9), rgba(205,205,205,0) 80%),
      linear-gradient(180deg, #f6f5f3, #e8e5e0 60%, #d6cfc4);
  }
</style>
</head>
<body>
  <header class="site-header">
    <div class="brand">Morvel Brew Supply</div>
    <nav class="main-nav">
      <a class="is-active" href="#" style="left:569px">HOME</a>
      <a href="#" style="left:634px">COFFEE &amp; TEA</a>
      <a href="#" style="left:743px">CONDIMENTS</a>
      <a href="#" style="left:848px">PAPER &amp; PLASTICS</a>
      <a href="#" style="left:984px">CONTACT</a>
    </nav>
  </header>

  <section class="hero" role="img" aria-label="Burlap sack of roasted coffee beans with three metal scoops">
    <div class="hero-caption">Only the freshest, highest-quality in-room coffee available</div>
  </section>

  <article class="product-card" style="left:159px">
    <h2>COFFEE</h2>
    <div class="product-photo photo-coffee" role="img" aria-label="Canister of fresh roasted ground coffee"></div>
  </article>
  <article class="product-card" style="left:459px">
    <h2>TEA</h2>
    <div class="product-photo photo-tea" role="img" aria-label="Box of decaffeinated tea with tea bags"></div>
  </article>
  <article class="product-card" style="left:759px">
    <h2>CONDIMENTS</h2>
    <div class="product-photo photo-condiments" role="img" aria-label="Sugar and creamer packets in a coffee mug"></div>
  </article>
</body>
</html>
```